Relaunch kelvorin.com

I need someone to review my existing site at WordPress, make it more contemporary and visually appealing while preserving the content, which is quite text-dense, and improve the navigation. For example, if you go to https://kelvorin.com/claims-handled/ you will see links to dedicated pages for various client groups - I would like those to somehow be evident from the home page.

It would be simpler to keep it at WordPress but I am open to using a different CMS if necessary.

Fluency in Spanish would be useful, since part of the site is in Spanish.

Target Market(s)

Shipowners, vessel operators, ship managers

Industry/Entity Type

Marine insurance / marine transportation

Number of Pages Required

5+ page

Colors

Designer to choose colors to be used in the design.

Requirements
Must have
• Substantially preserve exciting content, but make it more accessible.
Nice to have
• This is an online brochure - we don't sell anything on line. I would like the theme to tie in to the colors in the existing logo, which we will keep.

```html
<!DOCTYPE html>
<html lang="en">
<head>
<meta charset="utf-8">
<title>The Kelvorin Company – Average Adjusters</title>
<link rel="stylesheet" href="https://fonts.googleapis.com/css2?family=Lobster&family=Roboto:wght@300;400;500;700&display=swap">
<style>
:root{
  --red:#9b3a2b;
  --blue:#4e5b8c;
  --navy:#061a3d;
  --hero-blue:#1d5fb8;
  --text:#3a3a3a;
  --muted:#666;
  --paper:#f8f8fa;
  --contact-bg:#b8c3d6;
  --white:#ffffff;
}
*{box-sizing:border-box;margin:0;padding:0}
html,body{width:1200px;height:3525px;overflow:hidden}
body{font-family:"Roboto",Arial,sans-serif;color:var(--text);background:var(--white);position:relative}
.script{font-family:"Lobster",cursive;font-weight:400}
.btn{position:absolute;display:inline-flex;align-items:center;justify-content:center;height:37px;padding:0 24px;border-radius:20px;background:var(--red);color:var(--white);font:700 14px "Roboto",Arial,sans-serif;text-transform:uppercase;letter-spacing:.2px}
.btn--light{background:var(--white);color:var(--red)}

/* header */
.site-header{position:absolute;top:0;left:0;width:1200px;height:83px;background:var(--white);border-top:3px solid var(--red)}
.brand{position:absolute;left:146px;top:26px;font:700 30px "Roboto",Arial,sans-serif;color:var(--red);letter-spacing:1px}
.main-nav{position:absolute;left:363px;top:0;height:80px;display:flex;font-size:13.5px;font-weight:500;color:#333}
.main-nav a{display:flex;align-items:center;padding:0 12px;height:74px}
.main-nav a.active{background:var(--red);color:var(--white);padding:0 10px}
.lang{position:absolute;top:34px;width:20px;height:20px;border-radius:50%}
.lang--es{left:911px;background:#c8352b}
.lang--en{left:941px;background:#2e3f8a}
.panic{position:absolute;left:974px;top:26px;width:81px;height:37px;border-radius:20px;background:var(--blue);color:var(--white);font:500 15px "Roboto",Arial,sans-serif;display:flex;align-items:center;justify-content:center}

/* hero */
.hero{position:absolute;top:83px;left:0;width:1200px;height:500px;background:radial-gradient(ellipse at 65% 40%,#3a8de6 0%,var(--hero-blue) 30%,#0a2e6b 60%,var(--navy) 100%)}
.hero__title{position:absolute;left:144px;top:130px;font-size:64px;color:var(--white);text-shadow:0 3px 6px rgba(0,0,0,.5)}
.hero__lead{position:absolute;left:144px;top:225px;font-size:19px;color:var(--white)}
.hero .btn{left:144px;top:277px;border:2px solid var(--white)}
.hero__dots{position:absolute;left:80px;top:188px;display:flex;flex-direction:column;gap:11px}
.hero__dots span{width:10px;height:10px;border-radius:50%;background:#9aa3b4}
.hero__dots span.on{background:var(--white)}
.hero__curve{position:absolute;left:0;bottom:0}

/* welcome */
.welcome{position:absolute;top:583px;left:0;width:1200px;height:457px;background:var(--paper);text-align:center}
.welcome__title{position:absolute;top:0;left:0;width:100%;line-height:58px;font-size:52px}
.welcome__title .a{color:var(--blue);display:block}
.welcome__title .b{color:var(--red);display:block}
.welcome__body{position:absolute;left:186px;top:146px;width:828px;font-size:14.2px;line-height:24px;color:var(--text)}
.welcome__body p+p{margin-top:26px}
.welcome .btn{left:535px;top:346px;width:130px}

/* feature bands */
.band{position:absolute;left:0;width:1200px;height:475px;overflow:hidden}
.band--claims{top:1040px;background:var(--blue)}
.band--average{top:1515px;background:var(--red)}
.band__art{position:absolute;top:0}
.band__title{position:absolute;font-size:50px;color:var(--white)}
.band__text{position:absolute;font-size:14.2px;line-height:24px;color:var(--white);text-align:justify}
.band--claims .band__title{left:144px;top:60px}
.band--claims .band__text{left:144px;top:144px;width:382px}
.band--claims .btn{left:144px;top:361px;width:130px}
.band--average .band__title{left:667px;top:68px}
.band--average .band__text{left:668px;top:144px;width:382px}
.band--average .btn{left:668px;top:362px;width:130px}

/* staff */
.staff{position:absolute;top:1990px;left:0;width:1200px;height:612px;background:var(--paper)}
.staff__title{position:absolute;top:80px;left:0;width:100%;text-align:center;font-size:52px}
.staff__title .a{color:var(--blue)}
.staff__title .b{color:var(--red)}
.staff__photo{position:absolute;left:162px;top:200px}
.staff__name{position:absolute;left:561px;top:203px;font-size:24px;font-weight:500;color:#222}
.staff__bio{position:absolute;left:561px;top:250px;width:476px;font-size:14px;font-weight:300;line-height:27px;color:var(--muted);text-align:justify}
.staff .btn{left:561px;top:492px;width:130px}

/* contact */
.contact{position:absolute;top:2602px;left:0;width:1200px;height:555px;background:linear-gradient(180deg,var(--contact-bg) 0%,#cfd7e4 60%,#bcc6d6 100%)}
.contact__title{position:absolute;top:70px;left:0;width:100%;text-align:center;font-size:52px;color:var(--blue)}
.contact__title .b{color:var(--red)}
.field{position:absolute;background:var(--white);font-size:15.5px;color:#555;padding:0 21px;display:flex;align-items:center;height:52px}
.field--msg{align-items:flex-start;padding-top:19px;height:115px}
.contact .btn{left:535px;top:438px;width:130px}

/* footer */
.site-footer{position:absolute;top:3157px;left:0;width:1200px;height:368px;background:var(--white);border-bottom:4px solid var(--red)}
.info{position:absolute;top:72px;display:flex;align-items:center;gap:12px;font-size:14.5px;line-height:20px;color:#333}
.info__icon{width:41px;height:41px;border-radius:50%;display:flex;align-items:center;justify-content:center;flex:none}
.info__icon--blue{background:var(--blue)}
.info__icon--red{background:var(--red)}
.divider{position:absolute;top:60px;width:1px;height:65px;background:#ccc}
.footer-nav{position:absolute;top:165px;left:0;width:100%;display:flex;justify-content:center;gap:26px;font-size:15.5px;font-weight:500;color:#333;text-transform:uppercase}
.copyright{position:absolute;top:220px;left:0;width:100%;text-align:center;font-size:13.5px;color:#444}
.social{position:absolute;top:274px;width:43px;height:43px;border-radius:50%}
.social--one{left:554px;background:var(--red)}
.social--two{left:604px;background:var(--blue)}
</style>
</head>
<body>

<header class="site-header">
  <div class="brand">KELVORIN</div>
  <nav class="main-nav">
    <a class="active">Home</a>
    <a>Claims Handled</a>
    <a>General Average</a>
    <a>Staff</a>
    <a>Resources</a>
    <a>Contact Us</a>
  </nav>
  <span class="lang lang--es" aria-label="Español"></span>
  <span class="lang lang--en" aria-label="English"></span>
  <div class="panic">PANIC</div>
</header>

<section class="hero" role="img" aria-label="Photograph of a glowing blue globe with network connections across the world">
  <div class="hero__dots"><span></span><span class="on"></span><span></span></div>
  <h1 class="hero__title script">The Kelvorin Company</h1>
  <p class="hero__lead">Average adjusters and marine insurance consultants</p>
  <span class="btn">Get Started</span>
  <svg class="hero__curve" width="1200" height="80" viewBox="0 0 1200 80">
    <path d="M0 80 C300 10 800 -10 1200 40 L1200 80 Z" fill="#f8f8fa"/>
    <path d="M0 80 C300 10 800 -10 1200 40" fill="none" stroke="#4e5b8c" stroke-width="4"/>
  </svg>
</section>

<section class="welcome">
  <h2 class="welcome__title script"><span class="a">Welcome to</span><span class="b">The Kelvorin Company</span></h2>
  <div class="welcome__body">
    <p>The Kelvorin Company is a leading, independent average adjuster, in operation since 1998. We take pride in the speed of our response, the accuracy of our work, the reasonableness of our fees and the professional standards we uphold.</p>
    <p>“Average” is believed to derive from an old Arabic word, “awar”, meaning “damage”. For centuries, average was a mechanism for dividing the risk inherent to a maritime adventure, with each merchant sharing in proportion to the profit, in the case of success, or in proportion to the value of what was saved, if the ship and goods had fallen into peril. That mathematical operation, of dividing things proportionately, led to the more common, modern understanding of the word.</p>
  </div>
  <span class="btn">Read More</span>
</section>

<section class="band band--claims">
  <h2 class="band__title script">Claims Handled</h2>
  <p class="band__text">Here we briefly summarize the types of claim we principally handle. If you don’t see what you are looking for, tell us and we can discuss whether we can conscientiously take it on. Successful claim outcomes revolve around a combination of factors, including thinking clearly, writing clearly, communicating clearly with assureds about underwriters’ expectations and ensuring that surveyors produce coherent and comprehensive reports.</p>
  <span class="btn">Read More</span>
  <svg class="band__art" style="left:590px" width="610" height="475" viewBox="0 0 610 475" role="img" aria-label="Photograph of two business people reviewing documents at a desk">
    <defs><linearGradient id="deskTone" x1="0" y1="0" x2="1" y2="1"><stop offset="0" stop-color="#e9edf1"/><stop offset=".5" stop-color="#c9d0d8"/><stop offset="1" stop-color="#f2f4f6"/></linearGradient></defs>
    <path d="M50 0 C-10 150 -10 330 60 475 L610 475 L610 0 Z" fill="url(#deskTone)"/>
    <path d="M50 0 C-10 150 -10 330 60 475" fill="none" stroke="#ffffff" stroke-width="4"/>
  </svg>
</section>

<section class="band band--average">
  <svg class="band__art" style="left:0" width="610" height="475" viewBox="0 0 610 475" role="img" aria-label="Illustration of a shield holding stacked shipping containers with a cargo ship at sunset">
    <defs><linearGradient id="seaTone" x1="0" y1="0" x2="0" y2="1"><stop offset="0" stop-color="#f0c9a0"/><stop offset=".5" stop-color="#b99a86"/><stop offset="1" stop-color="#6f8aa3"/></linearGradient></defs>
    <path d="M0 0 L555 0 C615 150 615 330 550 475 L0 475 Z" fill="url(#seaTone)"/>
    <path d="M555 0 C615 150 615 330 550 475" fill="none" stroke="#ffffff" stroke-width="4"/>
  </svg>
  <h2 class="band__title script">General Average</h2>
  <p class="band__text">General Average is a method of equitable distribution of the financial consequences of actions taken to preserve the property imperiled in a common maritime adventure. Almost universally, it is adjusted in accordance with a code called the Meridian Adjustment Code, of which an international maritime law body, the Harbourline Maritime Council (HMC), is custodian. The HMC publishes a very useful set of General Average Guidelines, designed to introduce</p>
  <span class="btn btn--light">Read More</span>
</section>

<section class="staff">
  <h2 class="staff__title script"><span class="a">Our</span> <span class="b">Staff</span></h2>
  <svg class="staff__photo" width="340" height="340" viewBox="0 0 340 340" role="img" aria-label="Portrait photograph of Adrian P. Holloway">
    <circle cx="168" cy="172" r="166" fill="#4e5b8c"/>
    <circle cx="178" cy="164" r="164" fill="#ffffff"/>
    <circle cx="178" cy="164" r="156" fill="#2a2d33"/>
  </svg>
  <h3 class="staff__name">Adrian P. Holloway</h3>
  <p class="staff__bio">Adrian Holloway began his career in Liverpool in 1979 with a regional average adjusting firm.&nbsp; He moved to New York in 1981 and has lived here ever since. In 1987, he became a Full Member, by examination, of the national guild of marine average adjusters. In 1999 he joined a large overseas marine insurer and opened a New York office for the group. Two years later, when that underwriter decided to concentrate its operations back home, Adrian returned to full-time average adjusting, this time for his own account.&nbsp; He became a US citizen in 2008.</p>
  <span class="btn">Read More</span>
</section>

<section class="contact">
  <h2 class="contact__title script">Contact <span class="b">Us</span></h2>
  <div class="field" style="left:234px;top:168px;width:360px">First Name</div>
  <div class="field" style="left:606px;top:168px;width:359px">Last Name</div>
  <div class="field" style="left:234px;top:233px;width:360px">Email address</div>
  <div class="field" style="left:606px;top:233px;width:359px">Phone Number</div>
  <div class="field field--msg" style="left:234px;top:298px;width:731px">Message</div>
  <span class="btn">Submit</span>
</section>

<footer class="site-footer">
  <div class="info" style="left:180px">
    <span class="info__icon info__icon--blue"><svg width="14" height="18" viewBox="0 0 14 18"><path d="M7 0C3 0 0 3 0 7c0 5 7 11 7 11s7-6 7-11c0-4-3-7-7-7z" fill="#fff"/><circle cx="7" cy="7" r="2.5" fill="#4e5b8c"/></svg></span>
    <span>1180 Harbor Ridge Road, Port<br>Calder, NY 10990, USA</span>
  </div>
  <div class="divider" style="left:488px"></div>
  <div class="info" style="left:519px">
    <span class="info__icon info__icon--red"><svg width="16" height="16" viewBox="0 0 24 24"><path d="M6.6 10.8c1.4 2.8 3.8 5.1 6.6 6.6l2.2-2.2c.3-.3.7-.4 1-.2 1.1.4 2.3.6 3.6.6.6 0 1 .4 1 1V20c0 .6-.4 1-1 1C10.6 21 3 13.4 3 4c0-.6.4-1 1-1h3.5c.6 0 1 .4 1 1 0 1.3.2 2.5.6 3.6.1.3 0 .7-.2 1z" fill="#fff"/></svg></span>
    <span>Phone: +1 (555) 014-2287</span>
  </div>
  <div class="divider" style="left:775px"></div>
  <div class="info" style="left:812px">
    <span class="info__icon info__icon--blue"><svg width="16" height="12" viewBox="0 0 16 12"><rect width="16" height="12" rx="1" fill="#fff"/><path d="M0 1l8 6 8-6" fill="none" stroke="#4e5b8c" stroke-width="1.5"/></svg></span>
    <span>E-mail: info@kelvorin.com</span>
  </div>
  <nav class="footer-nav">
    <span>Home</span><span>/</span><span>Claims Handled</span><span>/</span><span>General Average</span><span>/</span><span>Staff</span><span>/</span><span>Resources</span><span>/</span><span>Contact Us</span>
  </nav>
  <p class="copyright">© 2024 The Kelvorin Company – KELVORIN.All Rights Reserved &nbsp;|&nbsp; Privacy &nbsp;|&nbsp; Terms of Use</p>
  <span class="social social--one" aria-label="Messaging link"></span>
  <span class="social social--two" aria-label="Professional network link"></span>
</footer>

</body>
</html>
```